"Harbourline Motorworks" business that imports classic cars, motorbikes and boats from the USA needs a bus

We need a business card design for our new company based in Brisbane Australia called "Harbourline Motorworks". You designed our company logo which I have attached. We source and import American Classic, Muscle and Vintage cars for customers in Australia. We also do the same for motor bikes and we will eventually move into boats. The logo is a very strong one so we feel that the colours of the card can not detract from the logo but enhance it. The font needs to be professional but not boring. We are finding dream machines for people so it needs to feel strong and safe, yet fun and be very cool.

Industry/Entity Type

Business

Contact Information for Business Card

Owen Calloway

Brisbane, QLD
Australia
Mobile: +61471 265 034
Email: owen calloway@mailvista.net

Requirements
Must have
• Strong logo presence
• Identify what we do
Should not have
• don't want it to be cluttered with text

```html
<!DOCTYPE html>
<html lang="en">
<head>
<meta charset="utf-8">
<title>Harbourline Motorworks — Business Card</title>
<link href="https://fonts.googleapis.com/css2?family=Marcellus&display=swap" rel="stylesheet">
<style>
  :root {
    --navy: #1f2f66;
    --blue: #2b4b98;
    --blue-light: #4468b8;
    --red: #d5192b;
    --red-dark: #a60f1f;
    --white: #ffffff;
    --page: #ffffff;
  }
  html, body {
    margin: 0;
    width: 1200px;
    height: 500px;
    overflow: hidden;
    background: var(--page);
    font-family: "Marcellus", serif;
  }
  .canvas {
    position: relative;
    width: 1200px;
    height: 500px;
  }
  .card {
    position: absolute;
    width: 506px;
    height: 305px;
    background: var(--white);
    overflow: hidden;
    box-shadow: 4px 6px 10px rgba(0,0,0,0.18);
  }
  .card--front { left: 72px; top: 95px; }
  .card--back  { left: 652px; top: 100px; }

  .wave {
    position: absolute;
    inset: 0;
    width: 506px;
    height: 305px;
    z-index: 2;
  }

  .brand-name {
    position: absolute;
    left: 0;
    width: 506px;
    top: 62px;
    margin: 0;
    text-align: center;
    color: var(--navy);
    font-size: 31px;
    line-height: 38px;
    font-weight: 400;
    letter-spacing: 1px;
    z-index: 3;
  }
  .brand-mark {
    display: block;
    width: 22px;
    height: 22px;
    margin: 0 auto 10px;
    border-radius: 50%;
    background: var(--red);
  }

  .holder-name {
    position: absolute;
    left: 93px;
    top: 252px;
    margin: 0;
    color: var(--white);
    font-size: 35px;
    font-weight: 400;
    letter-spacing: 0.5px;
    z-index: 3;
  }

  .photo {
    position: absolute;
    width: 150px;
    height: 100px;
    border: 5px solid var(--navy);
    box-shadow: inset 0 0 0 3px var(--red);
    z-index: 1;
  }
  .photo--sedan  { left: 50px;  top: 16px; background: linear-gradient(160deg, #c9a070 0%, #8d8f86 45%, #556a86 100%); }
  .photo--detail { left: 171px; top: 90px; background: linear-gradient(180deg, #b9bcc2 0%, #4e5a78 55%, #283456 100%); }
  .photo--coupe  { left: 293px; top: 16px; background: linear-gradient(180deg, #d9c3a6 0%, #b59c80 55%, #3a3432 100%); }

  .contact {
    position: absolute;
    right: 134px;
    top: 234px;
    margin: 0;
    text-align: right;
    color: var(--white);
    font-size: 13.5px;
    line-height: 14.5px;
    font-style: normal;
    z-index: 3;
  }
</style>
</head>
<body>
<main class="canvas">

  <section class="card card--front" aria-label="Business card front">
    <svg class="wave" viewBox="0 0 506 305" aria-hidden="true">
      <defs>
        <linearGradient id="front-blue" x1="0" y1="0" x2="0" y2="1">
          <stop offset="0" stop-color="var(--navy)"/>
          <stop offset="0.45" stop-color="var(--blue)"/>
          <stop offset="1" stop-color="var(--blue-light)"/>
        </linearGradient>
        <linearGradient id="front-red" x1="0" y1="0" x2="1" y2="0">
          <stop offset="0" stop-color="var(--red-dark)"/>
          <stop offset="0.5" stop-color="var(--red)"/>
          <stop offset="1" stop-color="var(--red-dark)"/>
        </linearGradient>
      </defs>
      <path class="wave-blue" d="M0,130 C60,112 100,230 215,228 C320,226 410,196 506,204 L506,305 L0,305Z" fill="url(#front-blue)"/>
      <path class="wave-red" d="M0,112 C70,92 110,196 212,194 C305,192 420,156 506,140 L506,190 C420,200 320,228 215,236 C108,242 62,146 0,162Z" fill="url(#front-red)"/>
      <path class="wave-stripe" d="M0,132 C72,114 112,214 213,212 C310,210 420,174 506,164" fill="none" stroke="var(--white)" stroke-width="7"/>
      <path class="wave-line" d="M0,170 C65,156 110,244 215,242 C320,240 410,208 506,210" fill="none" stroke="var(--white)" stroke-width="1.5"/>
    </svg>

    <h1 class="brand-name"><span class="brand-mark"></span>Harbourline<br>Motorworks</h1>
    <p class="holder-name">Owen Calloway</p>
  </section>

  <section class="card card--back" aria-label="Business card back">
    <div class="photo photo--sedan" role="img" aria-label="Photo of a classic American sedan on a country road"></div>
    <div class="photo photo--detail" role="img" aria-label="Photo of a close-up of a classic car body panel"></div>
    <div class="photo photo--coupe" role="img" aria-label="Photo of a black vintage hot-rod coupe"></div>

    <svg class="wave" viewBox="0 0 506 305" aria-hidden="true">
      <defs>
        <linearGradient id="back-blue" x1="0" y1="0" x2="0" y2="1">
          <stop offset="0" stop-color="var(--navy)"/>
          <stop offset="0.45" stop-color="var(--blue)"/>
          <stop offset="1" stop-color="var(--blue-light)"/>
        </linearGradient>
        <linearGradient id="back-red" x1="0" y1="0" x2="1" y2="0">
          <stop offset="0" stop-color="var(--red-dark)"/>
          <stop offset="0.45" stop-color="var(--red)"/>
          <stop offset="1" stop-color="var(--red-dark)"/>
        </linearGradient>
      </defs>
      <path class="wave-blue" d="M0,205 C110,190 200,238 310,236 C400,234 440,170 470,140 C485,125 500,125 506,128 L506,305 L0,305Z" fill="url(#back-blue)"/>
      <path class="wave-red" d="M0,158 C100,140 200,196 300,200 C385,203 425,140 458,112 C478,96 500,100 506,106 L506,150 C480,140 450,180 420,205 C390,228 350,236 300,236 C200,236 100,196 0,210Z" fill="url(#back-red)"/>
      <path class="wave-stripe" d="M0,180 C100,162 200,214 300,216 C390,218 430,158 462,130 C480,116 500,118 506,124" fill="none" stroke="var(--white)" stroke-width="7"/>
      <path class="wave-line" d="M0,222 C110,206 210,250 310,248 C400,246 440,186 480,156 C492,148 502,148 506,150" fill="none" stroke="var(--white)" stroke-width="1.5"/>
    </svg>

    <address class="contact">
      Brisbane, QLD<br>
      Australia<br>
      Mobile: +61471 265 034<br>
      Email: owen calloway@mailvista.net
    </address>
  </section>

</main>
</body>
</html>
```